Fernlow - telephone directory add

We need simple artwork advertisement for insertion in a local yellow pages telephone directory
Design brief for telephone ads
This project is to provide a pair of 62mm high x 91mm wide ‘yellow page adds’ for our company to place in a local phone book.
• They should reflect the same theme
• They should be based on a white ‘knock out’ background (printed on yellow paper) and have one colour in addition to black.
• Fernlow is our trading name
• Main contact details are www.Fernlow-demo.gg, telephone 473518, sales@fernlow, social.fernlow-demo.gg/motorimports
• Our address is Varclette Lane, St Auberon, GY5 8QT
• First box
o Vehicle sales – (we would like to promote)
 Japanese Minivan specialist
 European & UK vehicles supplied at best prices
 Vans and light commercials available
 Trusted supplier with 20 years experience

• Second box
o Service and repairs to all models
 Popular £99 service health check
 Qualified mechanics
 Wheel alignment & Air conditioning
 Fleet servicing options

local readers

Automotive

• Design brief for telephone ads
• This project is to provide a pair of 62mm high x 91mm wide ‘yellow page adds’ for our company to place in a local phone book.
• • They should reflect the same theme
• • They should be based on a white ‘knock out’ background (printed on yellow paper) and have one colour in addition to black.
• • Fernlow is our trading name
• • Main contact details are www.Fernlow-demo.gg, telephone 473518, sales@fernlow, social.fernlow-demo.gg/motorimports
• • Our address is Varclette Lane, St Auberon, GY5 8QT
• • First box
• o Vehicle sales – (we would like to promote)
•  Japanese Minivan specialist
•  European & UK vehicles supplied at best prices
•  Vans and light commercials available
•  Trusted supplier with 20 years experience
• • Second box
• o Service and repairs to all models
•  Popular £99 service health check
•  Qualified mechanics
•  Wheel alignment & Air conditioning
•  Fleet servicing options
• see attached word doc
• • First box
• • Second box
•  Qualified mechanics

```html
<!DOCTYPE html>
<html lang="en">
<head>
<meta charset="utf-8">
<title>Fernlow – directory adverts</title>
<link rel="stylesheet" href="https://fonts.googleapis.com/css2?family=Carlito:wght@400;700&family=Michroma&display=swap">
<style>
  :root {
    --ink: #000000;
    --paper: #ffffff;
    --accent: #2d4fd6;
    --backdrop: #e2e2e2;
    --text: #111111;
  }
  * { box-sizing: border-box; margin: 0; padding: 0; }
  html, body { width: 960px; height: 1200px; overflow: hidden; }
  body {
    background: var(--backdrop);
    font-family: "Carlito", "Calibri", sans-serif;
    color: var(--text);
    position: relative;
  }
  .ad {
    position: absolute;
    left: 186px;
    width: 590px;
    height: 402px;
    background: var(--paper);
  }
  .ad--sales { top: 150px; }
  .ad--service { top: 670px; }

  .ad__header {
    position: absolute; top: 12px; left: 0; right: 0; height: 73px;
    background: var(--ink);
    display: flex; align-items: center; justify-content: center;
  }
  .brand {
    font-family: "Carlito", sans-serif;
    font-weight: 700;
    font-size: 30px;
    letter-spacing: 2px;
    color: var(--accent);
  }

  .ad__title {
    position: absolute; left: 0; right: 0; top: 94px;
    text-align: center;
    line-height: 1.2;
  }
  .ad__title span {
    display: inline-block;
    font-family: "Michroma", sans-serif;
    font-weight: 700;
    color: var(--ink);
    padding: 0 16px 3px;
    border-bottom: 4px solid var(--ink);
    -webkit-text-stroke: 0.6px var(--ink);
  }
  .ad--sales .ad__title span { font-size: 24px; }
  .ad--service .ad__title span { font-size: 25.5px; padding: 0 6px 3px; }

  .features {
    position: absolute; left: 0; right: 0; top: 146px;
    list-style: none; text-align: center;
  }
  .features li {
    height: 28.8px; line-height: 28.8px;
    font-size: 24px; font-weight: 400;
    white-space: nowrap;
    -webkit-text-stroke: 0.35px var(--text);
  }
  .features svg { width: 17px; height: 17px; vertical-align: -2px; margin-right: 11px; }

  .contacts {
    position: absolute; left: 0; right: 0; top: 269px;
    list-style: none; text-align: center; font-size: 14.5px;
  }
  .contacts li { height: 19px; line-height: 19px; white-space: nowrap; }
  .contacts svg { width: 10px; height: 10px; vertical-align: -1px; margin-right: 9px; }

  .ad__footer {
    position: absolute; top: 356px; left: 0; right: 0; height: 31px;
    background: var(--ink); color: var(--paper);
    display: flex; align-items: center; justify-content: center;
    font-size: 16px; letter-spacing: 0.3px;
  }
  .ad__footer svg { width: 18px; height: 18px; margin-right: 10px; }
</style>
</head>
<body>

<svg width="0" height="0" style="position:absolute">
  <defs>
    <symbol id="tick" viewBox="0 0 20 20">
      <path d="M17 8.5A7.5 7.5 0 1 1 13 3.3" fill="none" stroke="#000" stroke-width="1.8" stroke-linecap="round"/>
      <path d="M6.5 9.5l3 3 8-8" fill="none" stroke="#000" stroke-width="1.8" stroke-linecap="round" stroke-linejoin="round"/>
    </symbol>
    <symbol id="globe" viewBox="0 0 10 10">
      <circle cx="5" cy="5" r="4.6" fill="#000"/>
      <path d="M0.5 5h9M5 0.5v9M2 2.5h6M2 7.5h6" stroke="#fff" stroke-width="0.6"/>
    </symbol>
    <symbol id="phone" viewBox="0 0 10 10">
      <path d="M1 3.5C1 2 3 1.5 5 1.5S9 2 9 3.5L7.5 4.3 7 3.2H3L2.5 4.3z" fill="#000"/>
      <rect x="2.5" y="4.5" width="5" height="4" rx="0.6" fill="#000"/>
    </symbol>
    <symbol id="mail" viewBox="0 0 10 10">
      <rect x="0.5" y="2" width="9" height="6.5" fill="#000"/>
      <path d="M0.8 2.3L5 5.6 9.2 2.3M0.8 8.2L4 5M9.2 8.2L6 5" fill="none" stroke="#fff" stroke-width="0.6"/>
    </symbol>
    <symbol id="square" viewBox="0 0 10 10">
      <rect x="0.5" y="0.5" width="9" height="9" rx="1.5" fill="#000"/>
    </symbol>
    <symbol id="pin" viewBox="0 0 20 20">
      <path d="M10 16s-5-5-5-9a5 5 0 0 1 10 0c0 4-5 9-5 9z" fill="none" stroke="#fff" stroke-width="1.1"/>
      <circle cx="10" cy="7" r="1.8" fill="none" stroke="#fff" stroke-width="1.1"/>
      <ellipse cx="10" cy="17" rx="6.5" ry="1.8" fill="none" stroke="#fff" stroke-width="1.1"/>
    </symbol>
  </defs>
</svg>

<section class="ad ad--sales">
  <header class="ad__header"><span class="brand">Fernlow</span></header>
  <h2 class="ad__title"><span>Vehicle SALES</span></h2>
  <ul class="features">
    <li><svg><use href="#tick"/></svg>Japanese Minivan specialist</li>
    <li><svg><use href="#tick"/></svg>European &amp; UK vehicles supplied at best prices</li>
    <li><svg><use href="#tick"/></svg>Vans and light commercials available</li>
    <li><svg><use href="#tick"/></svg>Trusted supplier with <b>20 years experience</b></li>
  </ul>
  <ul class="contacts">
    <li><svg><use href="#globe"/></svg>www.Fernlow-demo.gg</li>
    <li><svg><use href="#phone"/></svg>473518</li>
    <li><svg><use href="#mail"/></svg>sales@fernlow</li>
    <li><svg><use href="#square"/></svg>social.fernlow-demo.gg/motorimports</li>
  </ul>
  <footer class="ad__footer"><svg><use href="#pin"/></svg>Varclette Lane, St Auberon, GY5 8QT</footer>
</section>

<section class="ad ad--service">
  <header class="ad__header"><span class="brand">Fernlow</span></header>
  <h2 class="ad__title"><span>Service and repairs to all models</span></h2>
  <ul class="features">
    <li><svg><use href="#tick"/></svg>Popular <b>£99</b> service health check</li>
    <li><svg><use href="#tick"/></svg>Qualified mechanics</li>
    <li><svg><use href="#tick"/></svg>Wheel alignment &amp; Air conditioning</li>
    <li><svg><use href="#tick"/></svg>Fleet servicing options</li>
  </ul>
  <ul class="contacts">
    <li><svg><use href="#globe"/></svg>www.Fernlow-demo.gg</li>
    <li><svg><use href="#phone"/></svg>473518</li>
    <li><svg><use href="#mail"/></svg>sales@fernlow</li>
    <li><svg><use href="#square"/></svg>social.fernlow-demo.gg/motorimports</li>
  </ul>
  <footer class="ad__footer"><svg><use href="#pin"/></svg>Varclette Lane, St Auberon, GY5 8QT</footer>
</section>

</body>
</html>
```